LoanHarbor
I need double sided standard sized Business Card [3.5" x 2"]
Select font that compliments logo font
Simple
Pawel Merrin
Vice President - Purchase Division
4718 Birchwood Lane, Suite 300
Costa Mesa, CA 92681
Toll 800.517.2094
Direct 714.390.8152
Cell 949.306.7428
EFax 877.614.9087
pawelmerrin@loanharbor-example.net
www.loanharbor-example.net
NMLS# 748159
use periods in phone numbers instead of dashes. I like clean, aligned information and a lot of "negative" space. I want 2 versions one for the white background on white card, and one for the black background on a black card. Black card will be white on flip side.
This side is in the works. Will post very soon. Verbage.for both cards will be the same.

```html
<!DOCTYPE html>
<html lang="en">
<head>
<meta charset="utf-8">
<title>LoanHarbor Stationery</title>
<link rel="stylesheet" href="https://fonts.googleapis.com/css2?family=Open+Sans:wght@400;600;700&display=swap">
<style>
  :root{
    --bg:#e9e9e9;
    --paper:#ffffff;
    --ink:#2b3a4a;
    --muted:#7a8794;
    --brand:#1f7fc0;
    --brand-light:#5fb3e6;
    --night:#151515;
    --rule:#d5dbe0;
    --shadow:0 2px 5px rgba(0,0,0,.25);
  }
  *{box-sizing:border-box;margin:0;padding:0}
  html,body{width:1200px;height:310px;overflow:hidden;background:var(--bg);font-family:"Open Sans",Arial,sans-serif;color:var(--ink)}
  .canvas{position:relative;width:1200px;height:310px}
  .piece{position:absolute;background:var(--paper);box-shadow:var(--shadow);overflow:hidden}
  .piece svg.swoosh{position:absolute;left:0;bottom:0;width:100%}
  .brand{font-weight:700;color:var(--brand);letter-spacing:.2px;display:flex;align-items:center;gap:4px;white-space:nowrap}
  .brand .mark{display:inline-block;background:var(--brand)}
  .brand.on-dark{color:#fff}
  .brand.on-dark .mark{background:#fff}

  /* identity lockup */
  .lockup{position:absolute;left:24px;top:72px}
  .lockup .brand{font-size:24px;gap:8px}
  .lockup .brand .mark{width:18px;height:18px}

  /* business cards */
  .card{width:113px;height:41px}
  .card.dark{background:var(--night)}
  .card .brand{position:absolute;left:6px;top:6px;font-size:7px}
  .card .brand .mark{width:6px;height:6px}
  .card .info{position:absolute;right:5px;top:6px;font-size:3.2px;line-height:4.2px;text-align:right;color:var(--muted)}
  .card.dark .info{color:#bbb}
  .card .name{font-size:4.5px;font-weight:700;color:var(--ink)}
  .card.dark .name{color:#fff}
  .card.center .brand{left:0;right:0;top:13px;justify-content:center;font-size:10px}
  .card.center .brand .mark{width:9px;height:9px}

  /* letterheads */
  .letter{width:216px;height:276px;top:12px}
  .letter .brand{position:absolute;left:14px;top:14px;font-size:11px}
  .letter .brand .mark{width:8px;height:8px}
  .letter .contact{position:absolute;right:14px;top:14px;font-size:4px;line-height:5.4px;text-align:right;color:var(--muted)}
  .letter .footer{position:absolute;left:0;right:0;bottom:8px;text-align:center;font-size:4px;color:#fff}

  /* envelopes */
  .envelope{width:216px;height:72px}
  .envelope .brand{position:absolute;left:10px;top:8px;font-size:9px}
  .envelope .brand .mark{width:7px;height:7px}
  .envelope .return{position:absolute;left:10px;top:21px;font-size:3.5px;line-height:4.6px;color:var(--muted)}
  .envelope.back{background:#f4f6f8}
  .envelope.back .flap{position:absolute;inset:0}
</style>
</head>
<body>
<main class="canvas">

  <div class="lockup"><span class="brand"><span class="mark"></span>LoanHarbor</span></div>

  <!-- business cards -->
  <section class="piece card front" style="left:19px;top:127px">
    <span class="brand"><span class="mark"></span>LoanHarbor</span>
    <div class="info" style="top:17px">
      <div class="name">Pawel Merrin</div>
      Vice President - Purchase Division<br>
      4718 Birchwood Lane, Suite 300 · Costa Mesa, CA 92681
    </div>
    <svg class="swoosh" viewBox="0 0 113 8" preserveAspectRatio="none" height="6"><path d="M0 8 Q60 0 113 4 L113 8Z" fill="var(--brand)"/></svg>
  </section>

  <section class="piece card dark" style="left:139px;top:127px">
    <span class="brand on-dark"><span class="mark"></span>LoanHarbor</span>
    <div class="info" style="top:13px">
      <div class="name">Pawel Merrin</div>
      Toll 800.517.2094 · Direct 714.390.8152<br>
      Cell 949.306.7428 · EFax 877.614.9087<br>
      pawelmerrin@loanharbor-example.net<br>
      www.loanharbor-example.net · NMLS# 748159
    </div>
  </section>

  <section class="piece card center" style="left:19px;top:211px">
    <span class="brand"><span class="mark"></span>LoanHarbor</span>
    <svg class="swoosh" viewBox="0 0 113 8" preserveAspectRatio="none" height="6"><path d="M0 8 Q60 0 113 4 L113 8Z" fill="var(--brand)"/></svg>
  </section>

  <section class="piece card dark center" style="left:139px;top:211px">
    <span class="brand on-dark"><span class="mark"></span>LoanHarbor</span>
  </section>

  <!-- letterheads -->
  <section class="piece letter" style="left:264px">
    <span class="brand"><span class="mark"></span>LoanHarbor</span>
    <div class="contact">
      4718 Birchwood Lane, Suite 300<br>Costa Mesa, CA 92681<br>
      Toll 800.517.2094<br>Direct 714.390.8152<br>
      www.loanharbor-example.net
    </div>
    <svg class="swoosh" viewBox="0 0 216 34" preserveAspectRatio="none" height="34">
      <path d="M0 14 Q110 -2 216 10 L216 34 L0 34Z" fill="var(--brand-light)"/>
      <path d="M0 20 Q110 4 216 16 L216 34 L0 34Z" fill="var(--brand)"/>
    </svg>
    <div class="footer">www.loanharbor-example.net</div>
  </section>

  <section class="piece letter" style="left:492px">
    <span class="brand"><span class="mark"></span>LoanHarbor</span>
    <svg class="swoosh" viewBox="0 0 216 34" preserveAspectRatio="none" height="34">
      <path d="M0 14 Q110 -2 216 10 L216 34 L0 34Z" fill="var(--brand-light)"/>
      <path d="M0 20 Q110 4 216 16 L216 34 L0 34Z" fill="var(--brand)"/>
    </svg>
    <div class="footer">www.loanharbor-example.net</div>
  </section>

  <!-- envelopes -->
  <section class="piece envelope" style="left:720px;top:96px">
    <span class="brand"><span class="mark"></span>LoanHarbor</span>
    <div class="return">4718 Birchwood Lane, Suite 300<br>Costa Mesa, CA 92681</div>
    <svg class="swoosh" viewBox="0 0 216 16" preserveAspectRatio="none" height="16">
      <path d="M0 9 Q110 -2 216 6 L216 16 L0 16Z" fill="var(--brand)"/>
    </svg>
  </section>

  <section class="piece envelope" style="left:720px;top:192px;height:84px">
    <span class="brand"><span class="mark"></span>LoanHarbor</span>
    <div class="return">4718 Birchwood Lane, Suite 300<br>Costa Mesa, CA 92681</div>
    <svg class="swoosh" viewBox="0 0 216 18" preserveAspectRatio="none" height="18">
      <path d="M0 10 Q110 -2 216 7 L216 18 L0 18Z" fill="var(--brand)"/>
    </svg>
  </section>

  <!-- envelope stack -->
  <section class="piece envelope back" style="left:958px;top:60px;width:218px">
    <svg class="flap" viewBox="0 0 218 72" preserveAspectRatio="none">
      <path d="M0 0 L109 40 L218 0Z" fill="#8a8f95"/>
      <path d="M0 72 L109 34 L218 72" fill="none" stroke="var(--rule)" stroke-width="1"/>
    </svg>
  </section>
  <section class="piece envelope back" style="left:958px;top:120px;width:218px">
    <svg class="flap" viewBox="0 0 218 72" preserveAspectRatio="none">
      <path d="M0 0 L109 40 L218 0Z" fill="var(--brand)"/>
      <path d="M0 72 L109 34 L218 72" fill="none" stroke="var(--rule)" stroke-width="1"/>
    </svg>
  </section>
  <section class="piece envelope" style="left:958px;top:180px;width:218px">
    <span class="brand"><span class="mark"></span>LoanHarbor</span>
    <div class="return">4718 Birchwood Lane, Suite 300<br>Costa Mesa, CA 92681</div>
    <svg class="swoosh" viewBox="0 0 218 16" preserveAspectRatio="none" height="16">
      <path d="M0 9 Q110 -2 218 6 L218 16 L0 16Z" fill="var(--brand)"/>
    </svg>
  </section>

</main>
</body>
</html>
```